BRISK tuition homepage (After school courses)

We would like to introduce our tuition rates on new homepage. our website is www.brisklernhaus.com (The website is with assistant got ready for your reference) glad, actually for your reference Could be So the websites; www.lernwerkstube.de and www.wissensbogen.de -------------------- social media buttons must have; Facebook, twitter, youtube and Instagram --------------- for each page the customers Could send a short message or question through contact formula (as a reference you can find on the www.lernwerkstube. de "contact") ----------------- we want to add later on some pages short videos or youtube frames, the website must be therefore compatible with this aim) ---- ---------- The colors will be with the colors of the logo, background will be white.

Target Market(s)

Parents and students 10-18 jähre old

Industry/Entity Type

School

Coding

Coded - Design and coding required

Number of Pages Required

5+ page

Font styles to use
Sans Serif

Requirements
Must have
• Menus: - advantages (submenus: Elfogskonzept-qualified tutor-Individual counseling parents conversations-all benefits) - Courses (Elementary Promotion ZAP preparation-Abiturvorbereitung) - subjects (Math - German - English) - Education Package - BRISK places (HAGEN - ISERLOHN - SCHWERTE ) - KORBO Mental Arithmetic -Wortspiel4Mini ------------------------ For the menu "BRISK places": each googlemaps map with contact information ----- ----- must be compatible with tablets and the smartphones :-)
Should not have
• The header sliders must not cover whole screen

```html
<!DOCTYPE html>
<html lang="de">
<head>
<meta charset="utf-8">
<title>BRISK nachhilfe – Private Tuition</title>
<link rel="stylesheet" href="https://fonts.googleapis.com/css2?family=Arimo:wght@400;700&family=Montserrat:wght@300;400;500;600;700&display=swap">
<style>
:root{
  --blue:#27a6dd;
  --red:#ec4a57;
  --green:#8ec63f;
  --yellow:#fbb615;
  --text:#4a4a4a;
  --grey-card:#6a6a6a;
  --footer:#2e2e2e;
  --footer-bottom:#232323;
  --white:#fff;
  --fb:#1d5aa8;
  --tw:#1fa6e7;
  --yt:#d91b1b;
  --ig:#8a5a38;
  --gp:#e0422f;
  --body-font:"Arimo",Arial,sans-serif;
}
*{box-sizing:border-box;margin:0;padding:0}
html,body{width:1200px;height:2416px;overflow:hidden;background:var(--white)}
body{position:relative;font-family:"Montserrat",Arial,sans-serif;color:var(--text)}
.abs{position:absolute}

/* header */
.brand{left:0;width:1200px;top:14px;text-align:center}
.brand-name{display:inline-flex;align-items:center;gap:8px;font-size:22px;font-weight:500;color:#5a5a5a}
.brand-mark{width:22px;height:22px;background:var(--blue);border-radius:4px}
.brand-sub{font-size:8px;letter-spacing:3px;color:#777;margin-top:2px}
.nav{top:87px;left:195px;display:flex;height:42px}
.nav a{display:flex;align-items:center;justify-content:center;color:#fff;text-decoration:none;font-size:12px;font-weight:500;height:42px;margin-right:2px}
.nav .home{background:var(--blue);width:80px;height:50px;margin-top:-8px;padding-top:8px;clip-path:polygon(0 0,100% 10%,100% 100%,4% 100%)}

/* hero */
.hero{top:129px;left:0;width:1200px;height:457px;background:linear-gradient(90deg,#2a2a2a 0%,#454545 55%,#3c3c3c 100%)}
.hero-photo{left:590px;top:0;width:420px;height:457px;background:linear-gradient(180deg,#4a4a4a 0%,#9a7a62 45%,#5a5454 100%)}
.hero-title{left:195px;top:292px;font-size:25px;font-weight:600;color:#fff}
.hero-text{left:195px;top:333px;font-family:var(--body-font);font-size:13px;color:#e8e8e8}
.hero-btn{left:193px;top:357px;width:164px;height:39px;background:var(--yellow);color:#222;font-size:13px;font-weight:600;display:flex;align-items:center;justify-content:center;border-radius:2px}
.dots{left:208px;top:522px;display:flex;gap:8px}
.dots i{width:16px;height:16px;border-radius:50%;background:#cfcfcf;display:block}
.dots i.on{background:var(--yellow)}
.touch-label{left:1116px;top:234px;font-family:var(--body-font);font-size:12px;color:#fff;font-style:italic}
.touch{left:1148px;top:270px;width:52px}
.touch i{display:flex;align-items:center;justify-content:center;height:52px}
.touch i b{width:12px;height:12px;border-radius:2px;background:#fff}

/* sections */
.section-title{left:0;width:1200px;text-align:center;font-size:35px;font-weight:400;letter-spacing:1px}
.courses-title{top:620px;color:#5a5a5a}
.cards{left:179px;top:683px;width:842px;height:315px;display:flex}
.card{width:281px;height:315px;padding:9px 9px 0;overflow:hidden}
.card-img{height:161px}
.card h3{font-size:20px;font-weight:500;color:#fff;margin:17px 0 0 10px}
.card p{font-family:var(--body-font);font-size:10.5px;line-height:18px;color:#fff;margin:10px 8px 0 10px;text-align:justify}
.card.grey{background:var(--grey-card)} .card.grey .card-img{background:linear-gradient(#c7a47a,#8b4c3d)}
.card.blue{background:var(--blue)} .card.blue .card-img{background:linear-gradient(#e0b48c,#b04437)}
.card.red{background:var(--red)} .card.red .card-img{background:linear-gradient(#b9c2c6,#5b7a86)}

.feedback{top:1074px;left:0;width:1200px;height:454px;background:var(--green)}
.feedback-title{top:1100px;color:#fff}
.kid-art{left:298px;top:1150px;width:160px;height:340px;background:linear-gradient(#b7d88a,#a3cb6c)}
.cap-art{left:740px;top:1110px;width:186px;height:130px;background:linear-gradient(#9cc95c,#86b948)}
.video{left:444px;top:1175px;width:414px;height:303px;border:6px solid #cfe9a8;background:linear-gradient(#3b4a5a,#6e5a4e);box-shadow:0 2px 8px rgba(0,0,0,.3)}
.play{left:624px;top:1300px;width:50px;height:50px}

.team-title{top:1555px;color:#5a5a5a}
.team-lead{left:0;width:1200px;top:1616px;text-align:center;font-size:14px;line-height:26px;text-transform:uppercase;color:#444}
.member{top:1712px;width:300px;text-align:center}
.avatar{width:166px;height:166px;border-radius:50%;margin:0 auto;background:linear-gradient(#9a8478,#5c5c5c)}
.member h4{font-size:13px;font-weight:600;color:#222;margin-top:36px;letter-spacing:.5px}
.member p{font-family:var(--body-font);font-size:11px;line-height:21px;color:#555;margin-top:12px}
.icons{display:flex;justify-content:center;gap:14px;margin-top:18px}
.icons i{width:24px;height:24px;display:block}

/* footer */
.footer{top:2067px;left:0;width:1200px;height:300px;background:var(--footer)}
.links h5,.address h5{font-size:16px;font-weight:500;color:#fff}
.links{left:195px;top:2106px}
.links ul{list-style:none;margin-top:18px}
.links li{font-family:var(--body-font);font-size:10px;color:#ddd;line-height:22.5px}
.address{left:411px;top:2106px}
.address ul{list-style:none;margin-top:18px}
.address li{font-family:var(--body-font);font-size:11px;color:#ddd;line-height:29px;display:flex;align-items:center;gap:12px}
.map{left:412px;top:2236px;width:272px;height:108px;background:linear-gradient(135deg,#d6d6d6,#b9b9b9)}
.field{border:1px solid #bbb;color:#ddd;font-family:var(--body-font);font-size:9px;padding:8px}
.f-name{left:734px;top:2116px;width:147px;height:30px}
.f-mail{left:890px;top:2116px;width:147px;height:30px}
.f-msg{left:734px;top:2156px;width:303px;height:87px}
.send{left:734px;top:2254px;width:74px;height:29px;background:var(--red);color:#fff;font-family:var(--body-font);font-size:10px;display:flex;align-items:center;justify-content:center}
.foot-brand{left:880px;top:2290px;width:168px;text-align:center}
.foot-brand .brand-name{font-size:18px;color:#aaa}
.bottom{top:2367px;left:0;width:1200px;height:49px;background:var(--footer-bottom)}
.copy{top:2386px;left:0;width:1200px;text-align:center;font-family:var(--body-font);font-size:9px;color:#aaa}
.mark{top:2386px;left:1058px;font-family:var(--body-font);font-size:9px;color:#aaa}
</style>
</head>
<body>

<header>
  <div class="abs brand">
    <div class="brand-name"><span class="brand-mark"></span>brisknachhilfe</div>
    <div class="brand-sub">PRIVATE TUITION</div>
  </div>
  <nav class="abs nav">
    <a class="home">Home</a>
    <a style="background:var(--red);width:95px">Advantages</a>
    <a style="background:var(--green);width:88px">Courses</a>
    <a style="background:var(--yellow);width:69px">Subjects</a>
    <a style="background:var(--blue);width:146px">Education Package</a>
    <a style="background:var(--red);width:114px">BRISK places</a>
    <a style="background:var(--green);width:117px">KORBO Mental</a>
    <a style="background:var(--yellow);width:79px">Contact</a>
  </nav>
</header>

<section class="abs hero">
  <div class="abs hero-photo" role="img" aria-label="Photo of a schoolboy with glasses and bow tie in front of a chalkboard"></div>
</section>
<div class="abs hero-title">FREE VOUCHER FOR 2 HOURS *</div>
<div class="abs hero-text">Try our tuition suggested in Grupe instruction in small groups ...</div>
<div class="abs hero-btn">Request Voucher!</div>
<div class="abs dots"><i></i><i class="on"></i><i></i><i></i></div>
<div class="abs touch-label">Get in touch</div>
<div class="abs touch">
  <i style="background:var(--fb)"><b></b></i>
  <i style="background:var(--tw)"><b></b></i>
  <i style="background:var(--yt)"><b></b></i>
  <i style="background:var(--ig)"><b></b></i>
</div>

<h2 class="abs section-title courses-title">COURSES</h2>
<div class="abs cards">
  <article class="card grey">
    <div class="card-img" role="img" aria-label="Photo of a young pupil studying at a desk with books"></div>
    <h3>Elementary Promotion</h3>
    <p>Acquire them knowledge of glassblowing technique and shape molten glass by means of a blow pipe into a ball. They are continuously supervised and supported.</p>
  </article>
  <article class="card blue">
    <div class="card-img" role="img" aria-label="Photo of happy children in a classroom"></div>
    <h3>ZAP preparation</h3>
    <p>Ask your earthenware her own and impress your friends with your unique styles and creative results. You will learn to understand the entire process of pottery and can practically implement it.</p>
  </article>
  <article class="card red">
    <div class="card-img" role="img" aria-label="Photo of students working in a science lab"></div>
    <h3>Abiturvorbereitung</h3>
    <p>Be part of our creative group and learn to work with wood. Practice dealing with woodworking tools and learn the techniques of woodworking.</p>
  </article>
</div>

<section class="abs feedback"></section>
<h2 class="abs section-title feedback-title">FEEDBACK</h2>
<div class="abs kid-art" role="img" aria-label="Cartoon schoolboy pointing to the video"></div>
<div class="abs cap-art" role="img" aria-label="Graduation cap illustration"></div>
<div class="abs video" role="img" aria-label="Video still of students working with a teacher in a classroom"></div>
<svg class="abs play" viewBox="0 0 50 50"><circle cx="25" cy="25" r="22" fill="rgba(0,0,0,.35)" stroke="#fff" stroke-width="3"/><path d="M20 15 L35 25 L20 35 Z" fill="#fff"/></svg>

<h2 class="abs section-title team-title">OUR TEAM</h2>
<p class="abs team-lead">Eritatis et quasi architecto beatae vitae dicta sunt explicabo. Nemo enim<br>ipsam voluptatem quia voluptas sit aspernatur aut odit aut fugit, sed</p>

<div class="abs member" style="left:146px">
  <div class="avatar" role="img" aria-label="Portrait photo of team member Tobias Lenner"></div>
  <h4>TOBIAS LENNER</h4>
  <p>Lorem ipsum dolor sit amet, consectetur adipisicing<br>elit, sed do eiusmod tempor incididunt ut labore et</p>
  <div class="icons"><i style="background:var(--fb)"></i><i style="background:var(--tw)"></i><i style="background:var(--gp)"></i></div>
</div>
<div class="abs member" style="left:450px">
  <div class="avatar" role="img" aria-label="Portrait photo of team member Marina Feld"></div>
  <h4>MARINA FELD</h4>
  <p>Lorem ipsum dolor sit amet, consectetur adipisicing<br>elit, sed do eiusmod tempor incididunt ut labore et</p>
  <div class="icons"><i style="background:var(--fb)"></i><i style="background:var(--tw)"></i><i style="background:var(--gp)"></i></div>
</div>
<div class="abs member" style="left:755px">
  <div class="avatar" role="img" aria-label="Portrait photo of team member Karl Hausmann"></div>
  <h4>KARL HAUSMANN</h4>
  <p>Lorem ipsum dolor sit amet, consectetur adipisicing<br>elit, sed do eiusmod tempor incididunt ut labore et</p>
  <div class="icons"><i style="background:var(--fb)"></i><i style="background:var(--tw)"></i><i style="background:var(--gp)"></i></div>
</div>

<footer class="abs footer"></footer>
<div class="abs links">
  <h5>Quick Links</h5>
  <ul><li>Home</li><li>About Us</li><li>Advantages</li><li>Courses</li><li>Subjects</li><li>Education Package</li><li>BRISK places</li><li>KORBO Mental</li><li>Contact</li></ul>
</div>
<div class="abs address">
  <h5>Address</h5>
  <ul>
    <li><svg width="10" height="12" viewBox="0 0 10 12"><path d="M5 0a4 4 0 0 1 4 4c0 3-4 8-4 8S1 7 1 4a4 4 0 0 1 4-4z" fill="#ddd"/><circle cx="5" cy="4" r="1.5" fill="#2e2e2e"/></svg>69/A, Brisk nachhilfe.</li>
    <li><svg width="10" height="12" viewBox="0 0 10 12"><path d="M2 0h2l1 3-1.5 1a6 6 0 0 0 3 4L8 6.5l2 1V10c0 1-1 2-2 2C4 12 0 7 0 3 0 1 1 0 2 0z" fill="#ddd"/></svg>+49 2331 555 0192</li>
    <li><svg width="12" height="10" viewBox="0 0 12 10"><rect x=".5" y=".5" width="11" height="9" fill="none" stroke="#ddd"/><path d="M.5 .5 6 5.5 11.5 .5" fill="none" stroke="#ddd"/></svg>kontakt@brisklernhaus.com</li>
  </ul>
</div>
<div class="abs map" role="img" aria-label="Street map showing the school location"></div>
<div class="abs field f-name">Full Name</div>
<div class="abs field f-mail">E-mail Address</div>
<div class="abs field f-msg">Message</div>
<div class="abs send">Send</div>
<div class="abs foot-brand"><div class="brand-name"><span class="brand-mark"></span>brisknachhilfe</div></div>
<div class="abs bottom"></div>
<div class="abs copy">Copyright ©2016 www.brisklernhaus.com All Rights Reserved.</div>
<div class="abs mark">M1</div>

</body>
</html>
```